Office services

I need a post card that describes our office services that include Dr. Hollings credentials, services provided and website address, office address and phone number.
I have over 30 years of experience treating patients with chiropractic, acupuncture, and muscle release techniques.
Brandt graduate ( worlds largest chiropractic university)
Fellow, advanced and diplomate of needlework wellness guild of America.(highest certification possible)
Certified in Wexby decompression technique.
Pellman myofascial release certified.

Industry/Entity Type

Office

```html
<!DOCTYPE html>
<html lang="en">
<head>
<meta charset="utf-8">
<title>Fairbrook Chiropractor &amp; Acupuncture – Postcard</title>
<link rel="stylesheet" href="https://fonts.googleapis.com/css2?family=Open+Sans:ital,wght@0,400;0,600;0,700;1,400;1,600;1,700&display=swap">
<style>
  :root{
    --blue:#2aa7df;
    --blue-deep:#1b8ecb;
    --blue-pale:#7fcaf0;
    --black:#0e0e0e;
    --grey:#a7a9ac;
    --grey-text:#555a5e;
    --white:#ffffff;
    --caption:rgba(120,122,126,.82);
    --page:#ffffff;
  }
  *{box-sizing:border-box;margin:0;padding:0}
  html,body{width:1070px;height:1200px;overflow:hidden;background:var(--page)}
  body{position:relative;font-family:"Open Sans",Arial,sans-serif;color:var(--grey-text)}

  .card{position:absolute;background:var(--white);overflow:hidden;box-shadow:0 4px 14px rgba(0,0,0,.25)}
  .card--front{left:26px;top:20px;width:732px;height:555px}
  .card--back{left:274px;top:565px;width:766px;height:620px}
  .card__shapes{position:absolute;inset:0;width:100%;height:100%}

  .photo{position:absolute;overflow:hidden}
  .photo--skin{background:linear-gradient(135deg,#f3d3bd,#d9a488 60%,#c08a70)}
  .photo--needle{background:linear-gradient(160deg,#f1c9b0,#d99a7c 55%,#b9775e)}
  .photo--stone{background:linear-gradient(120deg,#f2dccb,#d8b7a0 50%,#8a6a5a)}
  .photo--portrait{background:radial-gradient(circle at 50% 45%,#e8c3a8,#b88a70 70%,#6f7f8c)}
  .photo--shoulder{background:linear-gradient(150deg,#e9eef2,#d6c1b3 45%,#c99f86)}
  .photo--teal{background:linear-gradient(160deg,#7fc4d2,#d9a58a 60%,#c9876a)}
  .photo--relax{background:linear-gradient(150deg,#f6e6da,#e2b79c 60%,#c98f73)}
  .caption{position:absolute;left:0;right:0;bottom:0;height:27px;background:var(--caption);color:var(--white);font-style:italic;font-weight:600;font-size:15px;line-height:27px;text-align:right;padding-right:18px}

  .quote-mark{position:absolute;font-family:Georgia,"Times New Roman",serif;font-weight:700;color:var(--white);line-height:1}
  .quote{position:absolute;color:var(--white);font-style:italic;line-height:1.3}
  .quote b{font-weight:700}

  .brand{position:absolute;display:flex;align-items:center;gap:18px}
  .brand__dot{border-radius:50%;background:var(--blue);flex:none}
  .brand__text{display:flex;flex-direction:column;color:var(--blue);line-height:1}
  .brand__name{font-weight:400;letter-spacing:1px;line-height:1}
  .brand__sub{font-weight:400;letter-spacing:.5px;line-height:1.2}
  .brand__tagline{color:var(--blue-pale);letter-spacing:1px;text-transform:uppercase;word-spacing:6px;line-height:1.3}

  .treat-list{position:absolute;list-style:none;font-size:14px;line-height:18px;color:var(--grey-text);columns:2;column-gap:38px;width:260px}
  .treat-list li{display:flex;align-items:center;gap:9px}
  .bullet{width:9px;height:12px;border-radius:50%/60% 60% 40% 40%;background:var(--blue);flex:none}

  .pill{position:absolute;background:var(--black);color:var(--white);font-weight:700;border-radius:14px;text-transform:uppercase;letter-spacing:.5px}

  .book{position:absolute;display:flex;align-items:center}
  .book__rule{position:absolute;height:2px;background:var(--blue)}
  .book__btn{position:relative;background:var(--blue);color:var(--white);font-size:15px;font-weight:600;border-radius:12px;padding:2px 18px 2px 30px;white-space:nowrap}
  .book__tick{position:absolute;left:-16px;top:-8px;width:34px;height:34px}

  .contact{position:absolute;display:flex;align-items:center;gap:6px;color:var(--grey-text);white-space:nowrap}
  .contact svg{flex:none}
  .contact--addr{font-size:13px}
  .contact--big{font-size:17px}

  .doctor-name{position:absolute;color:var(--white);font-style:italic;font-size:22px;font-weight:400}
  .cred-list{position:absolute;list-style:none;color:var(--white);font-size:11px;font-weight:600;font-style:italic;line-height:18px}
  .cred-list li{display:flex;align-items:center;gap:7px;white-space:nowrap}
  .cred-list .bullet{background:var(--white);width:8px;height:11px}
  .cred-list small{font-size:9px}
</style>
</head>
<body>

<!-- FRONT SIDE -->
<section class="card card--front">
  <svg class="card__shapes" viewBox="0 0 732 555" aria-hidden="true">
    <path d="M0 0 H470 C470 70 455 130 440 175 H0 Z" fill="var(--blue)"/>
    <path d="M476 0 H522 V175 H450 C470 120 480 60 476 0 Z" fill="var(--grey)"/>
    <path d="M490 300 C450 360 440 430 478 505 C492 460 505 420 522 395 V300 Z" fill="var(--blue)"/>
    <rect x="0" y="175" width="600" height="125" fill="var(--black)"/>
  </svg>

  <span class="quote-mark" style="left:28px;top:14px;font-size:88px">&ldquo;</span>
  <p class="quote" style="left:108px;top:38px;width:340px;font-size:16px">
    Chiropractic care <b>is more than just making the pain disappear.</b>
  </p>
  <p class="quote" style="left:108px;top:98px;width:340px;font-size:16px">
    It is about <b>learning, understanding and taking care of your body</b> to improve your quality of life.
  </p>

  <div class="photo photo--skin" role="img" aria-label="Photo of hands giving a chiropractic adjustment on a patient's back" style="left:522px;top:0;width:210px;height:202px;border-bottom-left-radius:40px">
    <span class="caption">Chiropractic</span>
  </div>
  <div class="photo photo--needle" role="img" aria-label="Photo of acupuncture needles placed in a patient's back" style="left:522px;top:208px;width:210px;height:177px">
    <span class="caption">Acupuncture</span>
  </div>
  <div class="photo photo--stone" role="img" aria-label="Photo of a woman relaxing during a hot stone massage" style="left:522px;top:391px;width:210px;height:164px">
    <span class="caption" style="bottom:20px">Massage Therapy</span>
  </div>

  <div class="brand" style="left:48px;top:192px">
    <span class="brand__dot" style="width:60px;height:60px"></span>
    <div class="brand__text">
      <span class="brand__name" style="font-size:56px">FAIRBROOK</span>
      <span class="brand__sub" style="font-size:16.5px;margin-top:4px">CHIROPRACTOR &amp; ACUPUNCTURE</span>
      <span class="brand__tagline" style="font-size:9px;margin-top:6px;margin-left:104px">Superior Chiropractic. Optimal Health.</span>
    </div>
  </div>

  <ul class="treat-list" style="left:44px;top:322px">
    <li><span class="bullet"></span>Headaches</li>
    <li><span class="bullet"></span>Migraine</li>
    <li><span class="bullet"></span>Neck Pain</li>
    <li><span class="bullet"></span>Back Pain</li>
    <li><span class="bullet"></span>Sciatica</li>
    <li><span class="bullet"></span>Shoulder Pain</li>
    <li><span class="bullet"></span>Knee Pain</li>
    <li><span class="bullet"></span>Arthritis</li>
    <li><span class="bullet"></span>Rheumatoid</li>
    <li><span class="bullet"></span>Muscle Pain</li>
    <li><span class="bullet"></span>Stiffness</li>
    <li><span class="bullet"></span>Spasm.</li>
  </ul>
  <span class="pill" style="left:322px;top:348px;font-size:15px;padding:3px 14px;transform:rotate(-6deg)">We Treat</span>

  <div class="book__rule" style="left:20px;top:466px;width:410px"></div>
  <div class="book" style="left:112px;top:454px">
    <span class="book__btn">
      <svg class="book__tick" viewBox="0 0 34 34" aria-hidden="true"><circle cx="15" cy="18" r="12" fill="var(--white)" stroke="var(--grey-text)" stroke-width="3"/><path d="M8 17 L15 24 L31 4" fill="none" stroke="var(--grey-text)" stroke-width="4" stroke-linecap="round" stroke-linejoin="round"/></svg>
      Book Appointment TODAY
    </span>
  </div>

  <p class="contact contact--addr" style="left:58px;top:480px">
    <svg width="12" height="16" viewBox="0 0 12 16" aria-hidden="true"><path d="M6 0 A6 6 0 0 1 12 6 C12 10 6 16 6 16 C6 16 0 10 0 6 A6 6 0 0 1 6 0 Z" fill="var(--blue)"/><circle cx="6" cy="6" r="2.3" fill="var(--white)"/></svg>
    2480 W. Lanternwood Dr. Ste.204, Fairbrook, IL 60000
  </p>
  <p class="contact contact--big" style="left:40px;top:508px">
    <svg width="20" height="18" viewBox="0 0 20 18" aria-hidden="true"><rect x="0" y="1" width="20" height="16" rx="2" fill="var(--blue)"/><rect x="3" y="4" width="4" height="10" rx="1" fill="var(--white)"/><rect x="9" y="4" width="8" height="3" fill="var(--white)"/><rect x="9" y="9" width="3" height="2" fill="var(--white)"/><rect x="14" y="9" width="3" height="2" fill="var(--white)"/><rect x="9" y="12" width="3" height="2" fill="var(--white)"/><rect x="14" y="12" width="3" height="2" fill="var(--white)"/></svg>
    (555) 014-2273
  </p>
  <p class="contact contact--big" style="left:210px;top:508px">
    <svg width="19" height="19" viewBox="0 0 20 20" aria-hidden="true"><circle cx="10" cy="10" r="9.5" fill="var(--blue)"/><path d="M10 .5 C6 5 6 15 10 19.5 M10 .5 C14 5 14 15 10 19.5 M.5 10 H19.5 M2.5 5 H17.5 M2.5 15 H17.5" fill="none" stroke="var(--white)" stroke-width="1.2"/></svg>
    www.DrHollingsCare.com
  </p>
</section>

<!-- BACK SIDE -->
<section class="card card--back">
  <svg class="card__shapes" viewBox="0 0 766 620" aria-hidden="true">
    <path d="M0 0 H600 C560 60 470 70 420 130 C380 190 380 300 410 408 H0 Z" fill="var(--blue)"/>
    <rect x="0" y="408" width="612" height="72" fill="var(--black)"/>
    <path d="M590 408 H626 V472 C590 478 548 488 505 506 C545 478 575 446 590 408 Z" fill="var(--blue)"/>
  </svg>

  <div class="photo photo--shoulder" role="img" aria-label="Photo of a woman receiving a shoulder massage" style="left:400px;top:110px;width:220px;height:298px;border-top-left-radius:150px"></div>
  <div class="photo photo--portrait" role="img" aria-label="Portrait photo of the doctor" style="left:468px;top:-12px;width:148px;height:148px;border-radius:50%;border:6px solid var(--white)"></div>

  <div class="photo photo--skin" role="img" aria-label="Photo of hands massaging a patient's back" style="left:626px;top:0;width:140px;height:120px"></div>
  <div class="photo photo--teal" role="img" aria-label="Photo of a therapist working on a patient" style="left:626px;top:126px;width:140px;height:164px;border-top-left-radius:50px"></div>
  <div class="photo photo--needle" role="img" aria-label="Photo of a back massage with oil" style="left:626px;top:296px;width:140px;height:112px"></div>
  <div class="photo photo--relax" role="img" aria-label="Photo of a smiling woman relaxing on a massage table" style="left:626px;top:414px;width:140px;height:160px;border-bottom-left-radius:50px"></div>

  <h2 class="doctor-name" style="left:32px;top:76px">Dr. Nolan Hollings</h2>
  <span class="pill" style="left:366px;top:94px;font-size:13px;padding:3px 12px">Credentials</span>

  <ul class="cred-list" style="left:40px;top:130px;transform:rotate(-4deg);transform-origin:0 100%">
    <li><span class="bullet"></span>DC – Doctor of Chiropractic Brandt College of Chiropractic</li>
    <li><span class="bullet"></span>Diplomate in Acupuncture</li>
    <li><span class="bullet"></span>Diplomate – <small>National Council of Spine Examiners</small></li>
    <li><span class="bullet"></span>Advanced Certification Needlework Wellness Guild of America</li>
    <li><span class="bullet"></span>FNWG – <small>Fellow of the Needlework Wellness Guild of America</small></li>
    <li><span class="bullet"></span>Certified in Wexby Decompression/Distraction Technique</li>
    <li><span class="bullet"></span>Certified in Pellman Myofascial Release Technique</li>
    <li><span class="bullet"></span>FASBE – <small>Fellow in Applied Spinal Biomechanical Engineering</small></li>
  </ul>

  <span class="quote-mark" style="left:64px;top:300px;font-size:72px">&ldquo;</span>
  <p class="quote" style="left:126px;top:294px;width:230px;font-size:15px;line-height:1.2">
    <b style="font-weight:600">Acupuncture and Chiropractic</b><br>
    <span style="font-size:13.5px">are like a brother and sister relationship.</span>
  </p>
  <p class="quote" style="left:134px;top:362px;font-size:14px">They go hand-in-hand for healing.</p>

  <div class="brand" style="left:180px;top:411px;gap:14px">
    <span class="brand__dot" style="width:46px;height:46px"></span>
    <div class="brand__text">
      <span class="brand__name" style="font-size:38px">FAIRBROOK</span>
      <span class="brand__sub" style="font-size:12px;margin-top:1px">CHIROPRACTOR &amp; ACUPUNCTURE</span>
      <span class="brand__tagline" style="font-size:7px;margin-left:60px;color:var(--blue-deep)">Superior Chiropractic. Optimal Health.</span>
    </div>
  </div>

  <div class="book__rule" style="left:80px;top:510px;width:410px"></div>
  <div class="book" style="left:250px;top:498px">
    <span class="book__btn">
      <svg class="book__tick" viewBox="0 0 34 34" aria-hidden="true"><circle cx="15" cy="18" r="12" fill="var(--white)" stroke="var(--grey-text)" stroke-width="3"/><path d="M8 17 L15 24 L31 4" fill="none" stroke="var(--grey-text)" stroke-width="4" stroke-linecap="round" stroke-linejoin="round"/></svg>
      Book Appointment TODAY
    </span>
  </div>

  <p class="contact contact--addr" style="left:190px;top:538px">
    <svg width="12" height="16" viewBox="0 0 12 16" aria-hidden="true"><path d="M6 0 A6 6 0 0 1 12 6 C12 10 6 16 6 16 C6 16 0 10 0 6 A6 6 0 0 1 6 0 Z" fill="var(--blue)"/><circle cx="6" cy="6" r="2.3" fill="var(--white)"/></svg>
    2480 W. Lanternwood Dr. Ste.204, Fairbrook, IL 60000
  </p>
  <p class="contact contact--big" style="left:166px;top:566px">
    <svg width="20" height="18" viewBox="0 0 20 18" aria-hidden="true"><rect x="0" y="1" width="20" height="16" rx="2" fill="var(--blue)"/><rect x="3" y="4" width="4" height="10" rx="1" fill="var(--white)"/><rect x="9" y="4" width="8" height="3" fill="var(--white)"/><rect x="9" y="9" width="3" height="2" fill="var(--white)"/><rect x="14" y="9" width="3" height="2" fill="var(--white)"/><rect x="9" y="12" width="3" height="2" fill="var(--white)"/><rect x="14" y="12" width="3" height="2" fill="var(--white)"/></svg>
    (555) 014-2273
  </p>
  <p class="contact contact--big" style="left:332px;top:566px">
    <svg width="19" height="19" viewBox="0 0 20 20" aria-hidden="true"><circle cx="10" cy="10" r="9.5" fill="var(--blue)"/><path d="M10 .5 C6 5 6 15 10 19.5 M10 .5 C14 5 14 15 10 19.5 M.5 10 H19.5 M2.5 5 H17.5 M2.5 15 H17.5" fill="none" stroke="var(--white)" stroke-width="1.2"/></svg>
    www.DrHollingsCare.com
  </p>
</section>

</body>
</html>
```